Upmarket building and construction company needs signage

Our building company R Brent Construction, needs signage to put up on the side of our vehicle trailers and on site fencing. We are a building company that specialises in residential construction and carpentry .

I will attach our logo and some inspirational pics for site fencing as well as what our trailer looks like .
Other details i would like on the sign are our
( email) rbrentconstruction@mailbox-example.net
(mobile ) 0493 518 264
(website ) rbrentconstruction. example.net

Target Market(s)

Home owners looking for a reliable local builder who produces good quality work. I have attached some inspirational pics.

Industry/Entity Type

Building and Construction

Colors

Designer to choose colors to be used in the design.

Requirements
Must have
• Our logo, contact information
Nice to have
• We would like the design to have elements of being Elegant, Serious, Modern, Professional, Masculine, Conservative and Upmarket.

```html
<!DOCTYPE html>
<html lang="en">
<head>
<meta charset="utf-8">
<title>R Brent Construction – Site Signage</title>
<link rel="stylesheet" href="https://fonts.googleapis.com/css2?family=Josefin+Sans:wght@300&family=Open+Sans:wght@700&family=Roboto:wght@400&family=Roboto+Condensed:wght@700&display=swap">
<style>
  :root {
    --backdrop: #2c2f33;
    --sign-grey: #8b8c90;
    --panel-white: #ffffff;
    --ink-grey: #7b7c80;
    --rule-grey: #8b8c90;
  }
  html, body {
    margin: 0;
    padding: 0;
    width: 1200px;
    height: 711px;
    overflow: hidden;
    background: var(--backdrop);
  }
  .canvas {
    position: relative;
    width: 1200px;
    height: 711px;
  }
  .sign {
    position: absolute;
    left: 40px;
    top: 163px;
    width: 1120px;
    height: 385px;
    background: var(--sign-grey);
  }
  .sign__edge-rule {
    position: absolute;
    left: 1080px;
    top: 0;
    width: 7px;
    height: 385px;
    background: var(--panel-white);
  }
  .sign__base-rule {
    position: absolute;
    left: -3px;
    top: 334px;
    width: 475px;
    height: 5px;
    background: var(--panel-white);
  }
  .brand {
    position: absolute;
    left: 70px;
    top: 150px;
    width: 260px;
    color: var(--panel-white);
    font-family: "Josefin Sans", sans-serif;
    font-weight: 300;
    text-align: center;
    line-height: 1;
  }
  .brand__name {
    display: block;
    font-size: 50px;
    letter-spacing: 2px;
    text-transform: uppercase;
  }
  .brand__suffix {
    display: block;
    margin-top: 8px;
    font-size: 27px;
    letter-spacing: 1px;
    text-transform: uppercase;
  }
  .contact-panel {
    position: absolute;
    left: 359px;
    top: 124px;
    width: 761px;
    height: 173px;
    background: var(--panel-white);
  }
  .contact-panel__email-row {
    position: absolute;
    left: 0;
    right: 60px;
    top: 30px;
    display: flex;
    align-items: center;
    gap: 16px;
  }
  .contact-panel__rule {
    flex: 1;
    height: 3px;
    background: var(--rule-grey);
  }
  .contact-panel__email {
    font-family: "Roboto", sans-serif;
    font-size: 20px;
    color: var(--ink-grey);
    white-space: nowrap;
  }
  .contact-panel__phone {
    position: absolute;
    right: 60px;
    top: 46px;
    margin: 0;
    font-family: "Open Sans", sans-serif;
    font-weight: 700;
    font-size: 82px;
    line-height: 1.2;
    color: var(--ink-grey);
    white-space: nowrap;
  }
  .sign__website {
    position: absolute;
    right: 60px;
    top: 322px;
    margin: 0;
    font-family: "Roboto Condensed", sans-serif;
    font-weight: 700;
    font-size: 29px;
    letter-spacing: 3px;
    line-height: 1;
    color: var(--panel-white);
    white-space: nowrap;
  }
</style>
</head>
<body>
  <main class="canvas">
    <section class="sign" aria-label="R Brent Construction site sign">
      <div class="sign__edge-rule"></div>

      <div class="brand">
        <span class="brand__name">R Brent</span>
        <span class="brand__suffix">Construction</span>
      </div>

      <div class="contact-panel">
        <div class="contact-panel__email-row">
          <span class="contact-panel__rule"></span>
          <span class="contact-panel__email">rbrentconstruction@mailbox-example.net</span>
        </div>
        <p class="contact-panel__phone">0493 518 264</p>
      </div>

      <div class="sign__base-rule"></div>
      <p class="sign__website">www.rbrentconstruction. example.net</p>
    </section>
  </main>
</body>
</html>
```